Hispanic Financial Counseling and Advocate Firm seeks business card design

Looking for a clean, professional business card design. This is a firm that specializes in providing financial education, coaching, and planning to the Hispanic community. The name of the company is Valemar, which means to prosper. We need a design that is clean, professional, and invokes trust, professionalism, but also welcoming. Our logo is a plant growing from a hand to give the messaging of of being in control of growing your financial future and security. Its part of a larger organization names Celesta Financial Group, who's logo is a tree with multi colored branches. We have the back of the card designed so we just need the front designed. the back is blue, so front needs to be a different background color, not blue.

Target Market(s)

Hispanic Community looking to better their future

Industry/Entity Type

financial services

Contact Information for Business Card

contact info: Anselmo Ibarra Jr, 951-555-0147, info@celestafinancialgroup.example. Celestafinancialgroup.example. tag line: Para un futuro mas seguro!

Requirements
Must have
• basics: logo, contact info.
Nice to have
• possibly incorporate the tree logo provided somehow
Should not have
• should not look like the back, needs to be different from the back provided.

```html
<!DOCTYPE html>
<html lang="es">
<head>
<meta charset="utf-8">
<title>Valemar – Tarjeta de presentación</title>
<link rel="stylesheet" href="https://fonts.googleapis.com/css2?family=Poppins:wght@500;600;700&display=swap">
<style>
  :root {
    --page-bg: #f1f2f4;
    --card-white: #ffffff;
    --slate: #4b5673;
    --leaf-green: #6cb33f;
    --text-light: #ffffff;
    --shadow: rgba(30, 35, 50, 0.28);
  }
  html, body {
    margin: 0;
    padding: 0;
    width: 867px;
    height: 1200px;
    overflow: hidden;
    background: var(--page-bg);
  }
  .stage {
    width: 867px;
    height: 1200px;
    display: flex;
    align-items: center;
    justify-content: center;
  }
  .business-card {
    width: 780px;
    height: 481px;
    display: block;
    background: var(--card-white);
    box-shadow: 0 10px 28px var(--shadow);
  }
  .business-card text {
    font-family: "Poppins", sans-serif;
  }
  .panel { fill: var(--slate); }
  .accent-stripe { fill: var(--leaf-green); }
  .gap-stripe { fill: var(--card-white); }
  .divider { stroke: var(--leaf-green); stroke-width: 2; }
  .brand-mark { fill: var(--leaf-green); }
  .brand-name { fill: var(--leaf-green); font-weight: 600; font-size: 104px; letter-spacing: -2px; }
  .brand-sub { fill: var(--slate); font-weight: 700; font-size: 25px; letter-spacing: 2.5px; }
  .tagline { fill: var(--text-light); font-weight: 600; font-size: 52px; }
  .person-first { fill: var(--leaf-green); font-weight: 700; font-size: 44px; letter-spacing: 1px; }
  .person-last { fill: var(--text-light); font-weight: 700; font-size: 44px; letter-spacing: 1px; }
  .contact-text { fill: var(--text-light); font-weight: 600; font-size: 26px; }
  .icon { fill: var(--leaf-green); }
  .icon-line { fill: none; stroke: var(--slate); stroke-width: 2.5; }
</style>
</head>
<body>
<main class="stage">
  <svg class="business-card" viewBox="0 0 1278 788" xmlns="http://www.w3.org/2000/svg" aria-label="Valemar business card front">
    <g class="wave">
      <path class="accent-stripe" transform="translate(-40 -4)" d="M120 788 C420 760 560 560 700 330 C820 130 1000 20 1278 0 L1278 788 Z"/>
      <path class="gap-stripe" transform="translate(-16 -1)" d="M120 788 C420 760 560 560 700 330 C820 130 1000 20 1278 0 L1278 788 Z"/>
      <path class="panel" d="M120 788 C420 760 560 560 700 330 C820 130 1000 20 1278 0 L1278 788 Z"/>
    </g>

    <g class="brand">
      <circle class="brand-mark" cx="272" cy="300" r="34"/>
      <text class="brand-name" x="272" y="460" text-anchor="middle">Valemar</text>
      <text class="brand-sub" x="272" y="506" text-anchor="middle">SERVICIOS FINANCIEROS</text>
    </g>

    <g class="tagline-block">
      <text class="tagline" x="1220" y="174" text-anchor="end">PARA UN</text>
      <text class="tagline" x="1220" y="226" text-anchor="end">FUTURO</text>
      <text class="tagline" x="1220" y="280" text-anchor="end">MAS SEGURO</text>
      <line class="divider" x1="783" y1="349" x2="1278" y2="349"/>
    </g>

    <g class="contact">
      <text x="662" y="482"><tspan class="person-first">ANSELMO</tspan><tspan class="person-last"> IBARRA JR</tspan></text>

      <g class="icon-phone" transform="translate(662 528)">
        <path class="icon" d="M6 2 C10 0 13 1 14 4 L17 11 C18 14 16 16 14 17 C16 22 20 26 25 28 C26 26 28 24 31 25 L37 28 C40 29 41 32 39 36 C36 40 31 41 26 38 C16 33 8 25 3 14 C1 9 2 5 6 2 Z"/>
      </g>
      <text class="contact-text" x="722" y="552">951-555-0147</text>

      <g class="icon-mail" transform="translate(662 590)">
        <rect class="icon" x="0" y="0" width="37" height="25"/>
        <path class="icon-line" d="M1 1 L18.5 14 L36 1 M1 24 L14 11 M36 24 L23 11"/>
      </g>
      <text class="contact-text" x="722" y="612">info@celestafinancialgroup.example</text>

      <g class="icon-globe" transform="translate(680 658)">
        <circle class="icon" cx="0" cy="0" r="18"/>
        <ellipse class="icon-line" cx="0" cy="0" rx="7" ry="18"/>
        <path class="icon-line" d="M-18 0 H18 M-15 -9 H15 M-15 9 H15 M0 -18 V18"/>
      </g>
      <text class="contact-text" x="722" y="668">Celestafinancialgroup.example</text>
    </g>
  </svg>
</main>
</body>
</html>
```